Social Media designs (LinkedIn banner, LinkedIn posts, Instagram)

Hello designers!
We are looking to create some more concepts for our social media identity for a search firm (recruitment company)
I have attached a "brand toolkit" that shows our brand, logo, colour scheme to guide you with regards to colours and identiy.

You will see in the brand toolkit there are some examples of;
- A LinkedIn banner for the company (page 23)
- Social Media posts for LinkedIn and Instagram (page 21)

What we are looking for...

We don't really like the current LinkedIn banner ideas. We would like to see more concepts that look more aesthetically pleasing - the current ideas look quite dull.

We DO like the social media post concepts but we would like to have more templates/options that we can use (similar themes)

We welcome submissions for Social Media designs that we can use with our company branding. Thank you for your work in advance!

```html
<!DOCTYPE html>
<html lang="en">
<head>
<meta charset="utf-8">
<title>Marlow Reed – Social Media Posts</title>
<link rel="stylesheet" href="https://fonts.googleapis.com/css2?family=Oswald:wght@500&family=Poppins:wght@400;500&display=swap">
<style>
  :root {
    --page: #ffffff;
    --card: #ffffff;
    --green: #4a8c72;
    --green-soft: #80b09a;
    --green-deep: #1c3a33;
    --green-mute: #2f4d45;
    --cream: #e6e3d6;
    --ink: #14201c;
    --photo-park-a: #6f9a63;
    --photo-park-b: #a54a45;
    --photo-office-a: #8d7a63;
    --photo-office-b: #4a3c30;
    --photo-glass-a: #2c4f7a;
    --photo-glass-b: #8fb3c9;
    --photo-team-a: #c9ccd3;
    --photo-team-b: #2b3040;
  }
  html, body { margin: 0; padding: 0; overflow: hidden; }
  body {
    width: 1200px; height: 843px; position: relative;
    background: var(--page);
    font-family: "Poppins", sans-serif;
  }
  .section-label {
    position: absolute; left: 166px; top: 22px; margin: 0;
    font: 400 16px "Poppins", sans-serif; letter-spacing: 0.5px; color: var(--ink);
  }
  .post-card {
    position: absolute; background: var(--card); border-radius: 10px;
    box-shadow: 0 2px 10px rgba(0,0,0,0.08); overflow: hidden;
  }
  .post-card svg { position: absolute; left: 0; display: block; }
  .headline { font-family: "Oswald", sans-serif; font-weight: 500; }
  .brand-name { font-family: "Poppins", sans-serif; font-weight: 500; }
  .copy { font-family: "Poppins", sans-serif; font-weight: 400; }
</style>
</head>
<body>
<svg width="0" height="0" style="position:absolute" aria-hidden="true">
  <defs>
    <linearGradient id="park" x1="0" y1="0" x2="0.4" y2="1">
      <stop offset="0" stop-color="var(--photo-park-a)"/>
      <stop offset="0.6" stop-color="#7f8b58"/>
      <stop offset="1" stop-color="var(--photo-park-b)"/>
    </linearGradient>
    <linearGradient id="office" x1="0" y1="0" x2="1" y2="1">
      <stop offset="0" stop-color="var(--photo-office-a)"/>
      <stop offset="1" stop-color="var(--photo-office-b)"/>
    </linearGradient>
    <linearGradient id="glass" x1="0" y1="0" x2="1" y2="0">
      <stop offset="0" stop-color="var(--photo-glass-b)"/>
      <stop offset="1" stop-color="var(--photo-glass-a)"/>
    </linearGradient>
    <linearGradient id="team" x1="0" y1="0" x2="0" y2="1">
      <stop offset="0" stop-color="var(--photo-team-a)"/>
      <stop offset="1" stop-color="var(--photo-team-b)"/>
    </linearGradient>
  </defs>
</svg>

<h1 class="section-label">social media post</h1>

<!-- Talent post, left column -->
<div class="post-card" style="left:148px;top:145px;width:234px;height:288px;">
  <svg style="top:34px" width="234" height="228" viewBox="0 0 450 440">
    <rect width="450" height="440" fill="var(--green)"/>
    <path role="img" aria-label="Photo of a smiling student sitting on grass in a park" d="M60 440 V290 C60 170 150 110 270 110 H450 V440 Z" fill="url(#park)"/>
    <path d="M270 440 C270 310 350 200 450 190 V440 Z" fill="var(--green)"/>
    <rect x="30" y="30" width="12" height="12" fill="var(--cream)"/>
    <text class="brand-name" x="52" y="58" font-size="44" fill="var(--cream)">Marlow</text>
    <text class="brand-name" x="52" y="102" font-size="44" fill="var(--cream)">Reed</text>
    <text class="headline" fill="var(--cream)"><tspan x="330" y="330" font-size="36">TALENT</tspan><tspan x="330" y="378" font-size="36">KNOWS</tspan><tspan x="330" y="412" font-size="22">NO BORDERS</tspan></text>
  </svg>
</div>

<!-- Case manager post, left column -->
<div class="post-card" style="left:148px;top:444px;width:234px;height:288px;">
  <svg style="top:34px" width="234" height="228" viewBox="0 0 450 440">
    <rect width="450" height="440" fill="var(--green-soft)"/>
    <path d="M0 0 H260 C120 40 40 160 40 270 V440 H0 Z" fill="var(--green)"/>
    <path role="img" aria-label="Photo of a glass office tower" d="M100 275 V170 C100 80 170 10 260 0 H310 V275 Z" fill="url(#glass)"/>
    <path d="M190 275 C190 180 260 110 350 110 H450 V275 Z" fill="var(--green-soft)"/>
    <rect role="img" aria-label="Photo of office tower windows" x="0" y="315" width="110" height="125" fill="url(#glass)"/>
    <path d="M230 275 H450 V440 H230 Z" fill="#ffffff"/>
    <path role="img" aria-label="Photo of office tower glass facade" d="M310 275 H322 V440 C260 430 225 370 225 300 V275 Z" fill="url(#glass)"/>
    <text class="headline" fill="var(--cream)" font-size="34"><tspan x="218" y="166">CASE MANAGER</tspan><tspan x="218" y="204">ENHANCED DUE</tspan><tspan x="218" y="242">DILIGENCE</tspan></text>
    <rect x="334" y="313" width="8" height="8" fill="var(--ink)"/>
    <text class="brand-name" x="347" y="321" font-size="14" fill="var(--ink)">Marlow Reed</text>
    <text class="headline" fill="var(--ink)" font-size="20"><tspan x="334" y="358">TALENT</tspan><tspan x="334" y="386">KNOWS</tspan><tspan x="334" y="414">NO BORDERS</tspan></text>
  </svg>
</div>

<!-- Talent post -->
<div class="post-card" style="left:521px;top:69px;width:253px;height:313px;">
  <svg style="top:38px" width="253" height="247" viewBox="0 0 450 440">
    <rect width="450" height="440" fill="var(--green)"/>
    <path role="img" aria-label="Photo of a smiling student sitting on grass in a park" d="M60 440 V290 C60 170 150 110 270 110 H450 V440 Z" fill="url(#park)"/>
    <path d="M270 440 C270 310 350 200 450 190 V440 Z" fill="var(--green)"/>
    <rect x="30" y="30" width="12" height="12" fill="var(--cream)"/>
    <text class="brand-name" x="52" y="58" font-size="44" fill="var(--cream)">Marlow</text>
    <text class="brand-name" x="52" y="102" font-size="44" fill="var(--cream)">Reed</text>
    <text class="headline" fill="var(--cream)"><tspan x="330" y="330" font-size="36">TALENT</tspan><tspan x="330" y="378" font-size="36">KNOWS</tspan><tspan x="330" y="412" font-size="22">NO BORDERS</tspan></text>
  </svg>
</div>

<!-- Announcement post -->
<div class="post-card" style="left:861px;top:69px;width:253px;height:313px;">
  <svg style="top:38px" width="253" height="247" viewBox="0 0 450 440">
    <rect width="450" height="440" fill="var(--green-deep)"/>
    <rect role="img" aria-label="Photo of colleagues stacking hands over a desk with newspapers" x="0" y="0" width="180" height="440" fill="url(#office)"/>
    <path d="M330 320 H445 V435 H330 Z" fill="var(--green-mute)"/>
    <rect x="198" y="40" width="12" height="12" fill="var(--cream)"/>
    <text class="brand-name" fill="var(--cream)" font-size="40"><tspan x="218" y="66">Marlow</tspan><tspan x="218" y="106">Reed</tspan></text>
    <text class="copy" fill="#ffffff" font-size="20" font-weight="500"><tspan x="197" y="155">ELIT DOLORE</tspan><tspan x="197" y="179">EXERCITATION CULPA</tspan><tspan x="197" y="203">OFFICIA 2023</tspan></text>
    <text class="copy" fill="#ffffff" font-size="13.5"><tspan x="200" y="246">Elit dolore exercitation</tspan><tspan x="200" y="261.5">culpa officia ea nostrud</tspan><tspan x="200" y="277">qui ea ut deserunt</tspan><tspan x="200" y="292.5">aliqua ullamco sed</tspan><tspan x="200" y="308">reprehenderit.</tspan><tspan x="200" y="323.5">Cupidatat ullamco, et</tspan><tspan x="200" y="339">adipisicing ipsum in est</tspan><tspan x="200" y="354.5">esse anim in dolor amet</tspan><tspan x="200" y="370">aute labore nulla cillum.</tspan><tspan x="200" y="385.5">Sed id sint adipisicing</tspan><tspan x="200" y="401">cupidatat laboris</tspan><tspan x="200" y="416.5">proident.</tspan></text>
  </svg>
</div>

<!-- Case manager post -->
<div class="post-card" style="left:522px;top:445px;width:252px;height:311px;">
  <svg style="top:37px" width="252" height="246" viewBox="0 0 450 440">
    <rect width="450" height="440" fill="var(--green-soft)"/>
    <path d="M0 0 H260 C120 40 40 160 40 270 V440 H0 Z" fill="var(--green)"/>
    <path role="img" aria-label="Photo of a glass office tower" d="M100 275 V170 C100 80 170 10 260 0 H310 V275 Z" fill="url(#glass)"/>
    <path d="M190 275 C190 180 260 110 350 110 H450 V275 Z" fill="var(--green-soft)"/>
    <rect role="img" aria-label="Photo of office tower windows" x="0" y="315" width="110" height="125" fill="url(#glass)"/>
    <path d="M230 275 H450 V440 H230 Z" fill="#ffffff"/>
    <path role="img" aria-label="Photo of office tower glass facade" d="M310 275 H322 V440 C260 430 225 370 225 300 V275 Z" fill="url(#glass)"/>
    <text class="headline" fill="var(--cream)" font-size="34"><tspan x="218" y="166">CASE MANAGER</tspan><tspan x="218" y="204">ENHANCED DUE</tspan><tspan x="218" y="242">DILIGENCE</tspan></text>
    <rect x="334" y="313" width="8" height="8" fill="var(--ink)"/>
    <text class="brand-name" x="347" y="321" font-size="14" fill="var(--ink)">Marlow Reed</text>
    <text class="headline" fill="var(--ink)" font-size="20"><tspan x="334" y="358">TALENT</tspan><tspan x="334" y="386">KNOWS</tspan><tspan x="334" y="414">NO BORDERS</tspan></text>
  </svg>
</div>

<!-- Team post -->
<div class="post-card" style="left:861px;top:445px;width:253px;height:313px;">
  <svg style="top:37px" width="253" height="249" viewBox="0 0 450 440">
    <rect width="450" height="440" fill="var(--cream)"/>
    <rect role="img" aria-label="Photo of a smiling business team at a meeting table" x="36" y="0" width="414" height="280" fill="url(#team)"/>
    <path d="M36 160 C90 230 170 270 300 260 C360 255 410 240 450 225 V440 H36 Z" fill="var(--cream)"/>
    <path d="M200 262 C290 250 380 215 450 200 V260 C380 265 300 275 200 262 Z" fill="var(--green-soft)" opacity="0.7"/>
    <rect x="0" y="0" width="36" height="440" fill="var(--green)"/>
    <rect x="46" y="24" width="10" height="10" fill="#ffffff"/>
    <text class="brand-name" fill="#ffffff" font-size="27"><tspan x="66" y="36">Marlow</tspan><tspan x="66" y="64">Reed</tspan></text>
    <text class="copy" fill="var(--ink)" font-weight="500"><tspan x="88" y="290" font-size="23">TALENT KNOWS</tspan><tspan x="88" y="320" font-size="28">NO BORDERS</tspan></text>
    <text class="copy" fill="var(--ink)" font-size="15"><tspan x="88" y="345">Elit dolore exercitation culpa officia ea</tspan><tspan x="88" y="362">nostrud qui ea ut deserunt aliqua ullamco</tspan><tspan x="88" y="379">sed reprehenderit. Cupidatat ullamco, et</tspan><tspan x="88" y="396">adipisicing ipsum in est esse anim in dolor</tspan><tspan x="88" y="413">amet aute labore nulla cillum. Sed id sint</tspan><tspan x="88" y="430">adipisicing cupidatat laboris proident.</tspan></text>
  </svg>
</div>
</body>
</html>
```